Boat and Caravan indoor/ outdoor storage

A new company that provides 4star indoor and outdoor storage for Boats and Caravans
Industry/Entity Type
It Company

```html
<!DOCTYPE html>
<html lang="en">
<head>
<meta charset="utf-8">
<title>The Harbour Shed – Boat &amp; Caravan Storage</title>
<link href="https://fonts.googleapis.com/css2?family=Antonio:wght@400;600&display=swap" rel="stylesheet">
<style>
  :root {
    --paper: #ffffff;
    --frame-blue: #2f4f9e;
    --poster-red: #e5322d;
    --poster-blue: #3d63b8;
    --navy: #1f2a5c;
    --light: #ffffff;
  }
  html, body {
    margin: 0;
    padding: 0;
    width: 851px;
    height: 1200px;
    overflow: hidden;
    background: var(--paper);
  }
  .poster {
    position: absolute;
    left: 23px;
    top: 23px;
    width: 805px;
    height: 1143px;
    box-sizing: border-box;
    border: 5px solid var(--frame-blue);
    background: var(--poster-red);
    overflow: hidden;
    font-family: "Antonio", "Arial Narrow", sans-serif;
    text-transform: uppercase;
    text-align: center;
  }
  .brand-title {
    position: absolute;
    left: 0; right: 0; top: 22px;
    margin: 0;
    font-weight: 400;
    font-size: 104px;
    line-height: 1;
    letter-spacing: 1px;
    color: var(--navy);
  }
  .tagline {
    position: absolute;
    left: 0; right: 0; top: 150px;
    margin: 0;
    font-weight: 400;
    font-size: 40px;
    line-height: 1;
    color: var(--light);
  }
  .boat-artwork {
    position: absolute;
    left: 0; right: 0; top: 205px;
    height: 360px;
    background: linear-gradient(180deg, var(--poster-red) 0%, var(--poster-blue) 45%, var(--poster-red) 70%, var(--poster-blue) 100%);
  }
  .about {
    position: absolute;
    left: 60px; right: 60px; top: 560px;
    margin: 0;
    font-size: 25px;
    line-height: 1.3;
    color: var(--light);
  }
  .contact-phone {
    position: absolute;
    left: 0; right: 0; top: 720px;
    margin: 0;
    font-size: 76px;
    line-height: 1;
    color: var(--navy);
  }
  .contact-email {
    position: absolute;
    left: 0; right: 0; top: 830px;
    margin: 0;
    font-size: 40px;
    line-height: 1;
    color: var(--navy);
    text-transform: none;
  }
  .contact-email .label { text-transform: uppercase; }
  .closing-band {
    position: absolute;
    left: 0; right: 0; bottom: 0;
    height: 250px;
    background: var(--poster-blue);
  }
  .closing-line {
    position: absolute;
    left: 0; right: 0; top: 55px;
    margin: 0;
    font-size: 44px;
    line-height: 1.4;
    color: var(--light);
  }
</style>
</head>
<body>
  <main class="poster">
    <h1 class="brand-title">The Harbour Shed</h1>
    <p class="tagline">5*****Indoor Boat/Caravan Storage</p>

    <div class="boat-artwork" role="img" aria-label="Posterised illustration of a motor cruiser boat in red and blue"></div>

    <p class="about">The Harbour Shed is based in Loughmore Co. Westvale. We provide excellent storage facilities in a fully secure environment. Outdoor storage and washing facilities are also available.</p>

    <p class="contact-phone">Tel: 00447700900123</p>
    <p class="contact-email"><span class="label">Email:</span> hello@harbourshed.com</p>

    <section class="closing-band">
      <p class="closing-line">A little luxury for your boat<br>and caravan at competitive rates</p>
    </section>
  </main>
</body>
</html>
```